Harbour Stone Advisory Double Sided DL Flyer

We need a double sided flyer that we provide to a Real Estate agent for leeds. It should provide our basic services as well as a modern look and feel. The brochure should incorporate our Brand colors and have a graphic that centres around money and property. I have included a couple of pictures that we like (but have not yet purchased from PIXVAULT) as an indication of the type of picture we like.

WE need to also show the Harbour Stone Advisory brand and have our Phone / address's and email details.

Target Market(s)

Realestate clients (Property Investors)

Industry/Entity Type

Financial Planning

Requirements
Must have
• Picture on Front (maybe the logo on back)
• Please incorporate existing logo colours.

```html
<!DOCTYPE html>
<html lang="en">
<head>
<meta charset="utf-8">
<title>Harbour Stone Advisory – DL Flyer</title>
<link href="https://fonts.googleapis.com/css2?family=Open+Sans:wght@400;600;700&family=Oswald:wght@500&display=swap" rel="stylesheet">
<style>
  :root{
    --green:#8cc63f;
    --green-dark:#6fa82a;
    --black:#141414;
    --charcoal:#2b2b2b;
    --ink:#1c1c1c;
    --white:#ffffff;
    --page:#e9e9e7;
  }
  *{box-sizing:border-box;margin:0;padding:0}
  html,body{width:1200px;height:1087px;overflow:hidden;background:var(--page)}
  body{position:relative;font-family:"Open Sans",Arial,sans-serif;color:var(--ink)}
  .flyer{
    position:absolute;top:76px;width:394px;height:826px;
    transform:scale(1.1548);transform-origin:top left;
    background:var(--white);overflow:hidden;
    box-shadow:0 2px 8px rgba(0,0,0,.18);
  }
  .flyer--front{left:137px}
  .flyer--back{left:655px}
  .flyer__art{position:absolute;inset:0;width:394px;height:826px}
  .brand{position:absolute;display:flex;align-items:center;gap:10px}
  .brand__mark{width:14px;height:14px;background:var(--green);flex:none}
  .brand__name{font-weight:700;color:var(--green);line-height:1.05;text-transform:uppercase;white-space:nowrap}
  .brand__tagline{position:absolute;font-size:7px;font-weight:700;color:var(--ink);letter-spacing:.1px;white-space:nowrap}
  .flyer--front .brand{left:26px;top:52px}
  .flyer--front .brand__name{font-size:25px}
  .flyer--front .brand__tagline{left:26px;top:118px}
  .flyer--back .brand{left:50px;top:28px}
  .flyer--back .brand__name{font-size:20px}
  .flyer--back .brand__tagline{left:50px;top:86px}

  .people{position:absolute;left:0;right:0;top:646px;text-align:center;color:var(--white)}
  .people__name{font-family:"Oswald",Impact,sans-serif;font-weight:500;font-size:23px;line-height:32px;letter-spacing:.2px}
  .people__role{font-size:17px;margin-top:4px}
  .phone-bar{position:absolute;left:0;right:0;top:752px;height:40px;background:var(--green);
    display:flex;align-items:center;justify-content:center;gap:8px;color:var(--white);
    font-family:"Oswald",Impact,sans-serif;font-size:20px;font-weight:500}

  .services{position:absolute;left:21px;right:14px;top:372px}
  .services__title{font-size:20px;line-height:26px;font-weight:400;color:var(--ink)}
  .services__list{list-style:none;margin-top:24px}
  .services__list li{position:relative;padding-left:22px;font-size:15.5px;line-height:32px;white-space:nowrap}
  .services__list li::before{content:"";position:absolute;left:0;top:11px;width:11px;height:11px;border-radius:50%;background:var(--green)}
  .services__list li::after{content:"";position:absolute;left:3px;top:14.5px;width:3px;height:3px;border-right:1.5px solid #fff;border-top:1.5px solid #fff;transform:rotate(45deg)}

  .contact{position:absolute;left:0;right:0;text-align:center;color:var(--white);font-size:13px}
  .contact--abn{top:680px}
  .contact--email{top:702px}
  .web-bar{position:absolute;left:0;right:0;top:731px;height:37px;background:var(--green);
    display:flex;align-items:center;justify-content:center;color:var(--white);font-size:13px}
  .addresses{position:absolute;left:0;right:0;top:776px;text-align:center;color:var(--white);font-size:13px;line-height:19px}
</style>
</head>
<body>

<section class="flyer flyer--front" aria-label="Flyer front">
  <svg class="flyer__art" viewBox="0 0 394 826">
    <defs>
      <radialGradient id="frontDark" cx="50%" cy="55%" r="60%">
        <stop offset="0" stop-color="#4a4a4a"/>
        <stop offset="1" stop-color="#121212"/>
      </radialGradient>
      <linearGradient id="frontPhoto" x1="0" y1="0" x2="1" y2="1">
        <stop offset="0" stop-color="#5f8f3a"/>
        <stop offset=".5" stop-color="#3f6e2a"/>
        <stop offset="1" stop-color="#8a6a4a"/>
      </linearGradient>
    </defs>
    <rect x="0" y="560" width="394" height="266" fill="url(#frontDark)"/>
    <path role="img" aria-label="Photo: hand watering a seedling in a jar of coins beside a small house model and coin stacks"
      d="M0 252 Q190 175 394 180 L394 530 Q200 605 0 612 Z" fill="url(#frontPhoto)"/>
    <path d="M0 242 Q190 160 394 166 L394 178 Q190 172 0 250 Z" fill="var(--green)"/>
    <path d="M0 612 Q200 605 394 530 L394 548 Q200 622 0 626 Z" fill="var(--green)"/>
    <path d="M0 630 Q200 628 394 556" stroke="#fff" stroke-width="3" fill="none"/>
  </svg>

  <div class="brand">
    <span class="brand__mark"></span>
    <span class="brand__name">Harbour Stone<br>Advisory</span>
  </div>
  <p class="brand__tagline">SOUND ADVICE FOR PROPERTY &amp; WEALTH</p>

  <div class="people">
    <p class="people__name">AARON WHITLOCK</p>
    <p class="people__name">CLARA HENSLEY</p>
    <p class="people__role">Advisor / Accountant</p>
  </div>
  <div class="phone-bar">
    <svg width="18" height="18" viewBox="0 0 24 24" aria-hidden="true"><circle cx="12" cy="12" r="10" fill="none" stroke="#fff" stroke-width="2"/><path d="M8.5 7l2 2.5-1.2 1.3c.7 1.5 1.8 2.6 3.2 3.3l1.3-1.2 2.5 2-1.2 1.6c-3.8-.6-6.8-3.6-7.4-7.4z" fill="#fff"/></svg>
    <span>(02) 5550 1842</span>
  </div>
</section>

<section class="flyer flyer--back" aria-label="Flyer back">
  <svg class="flyer__art" viewBox="0 0 394 826">
    <defs>
      <radialGradient id="backDark" cx="50%" cy="55%" r="60%">
        <stop offset="0" stop-color="#4a4a4a"/>
        <stop offset="1" stop-color="#121212"/>
      </radialGradient>
      <linearGradient id="backPhoto" x1="0" y1="0" x2="1" y2="0">
        <stop offset="0" stop-color="#dfe3e6"/>
        <stop offset=".55" stop-color="#c9d3dc"/>
        <stop offset="1" stop-color="#7f93a8"/>
      </linearGradient>
    </defs>
    <rect role="img" aria-label="Photo: hands holding a small white house model behind growing coin stacks with seedlings"
      x="0" y="112" width="394" height="256" fill="url(#backPhoto)"/>
    <path d="M0 720 Q180 640 394 652 L394 826 L0 826 Z" fill="url(#backDark)"/>
    <path d="M0 712 Q180 632 394 644 L394 652 Q180 642 0 722 Z" fill="var(--green)"/>
  </svg>

  <div class="brand">
    <span class="brand__mark"></span>
    <span class="brand__name">Harbour Stone<br>Advisory</span>
  </div>
  <p class="brand__tagline">SOUND ADVICE FOR PROPERTY &amp; WEALTH</p>

  <div class="services">
    <h2 class="services__title">Accountants and Financial Advisors<br>who specialise in:</h2>
    <ul class="services__list">
      <li>Negative Gearing &amp; Investment Properties</li>
      <li>Property &amp; Capital Gains Tax Minimisation</li>
      <li>Self-Managed Superannuation Funds (SMSF)</li>
      <li>Small Business &amp; Personal Taxation</li>
      <li>Investment Advice &amp; Risk Insurances</li>
    </ul>
  </div>

  <p class="contact contact--abn">ABN 47 912 384 105</p>
  <p class="contact contact--email">info@harbourstoneadvisory.com.au</p>
  <div class="web-bar">www.harbourstoneadvisory.com.au</div>
  <div class="addresses">
    <p>8 / 114 Tidewater Rd Bayview NSW 2250</p>
    <p>2 / 31 Marlin St Cove Point NSW 2263 (By Appointment)</p>
  </div>
</section>

</body>
</html>
```